Curtain Cleaning Flyer to be designed for Singapore market

We are a laundry company providing curtain cleaning services to Singapore market. We have a company vehicle pickup and provide dismantling of curtain at customer house. The dismantled curtain will be weighed and quote will be given to customer immediately. If they accept the price, we will delivered and installed the clean curtain to them.
Refer to our website for more information https://www.glintora.com.sg/curtain-cleaning
The flyer will be distributed to higher income level people in Singapore staying in condominium/semi detached or bungalow.
I need a well designed flyers to engage people to use my service. So please help.

Target Market(s)

Singapore market

Industry/Entity Type

It Company

Requirements
Must have
• MUST INCLUDE CURTAINS pictures in design to let people know it is for curtain laundry
• 1) Flyer has to be eye catching and engage people to call and use our curtain cleaning services.
• 2) It has to professional.
• 3) It has to provide clear information of the following (see curtain cleaning picture I have provided)
• Curtain Laundry at $10/kg
• Call 8362 4915
• No Hidden Cost
• Include Pickup, Dismantle, Installation and Delivery
• 4) Provide company information:
• KORU FLINT, Reg No.71846302K
• 47 Merrowby Lane
• Singapore 071934
• https://www.glintora.com.sg/curtain-cleaning
• Email: enquiries@glintora.com.sg
• Tel: +65 8362 4915
• 5) Include our company logo but do not use it extensively.
Nice to have
• Nice to have a compelling action design for people to call and use my service.
• Nice to highlight on the good laundry price $10 per kg for curtain laundry
• Nice to be professional and cute
Should not have
• Complicated
• No design on woman wearing low cut dresses for promotion

```html
<!DOCTYPE html>
<html lang="en">
<head>
<meta charset="utf-8">
<title>Curtain Laundry – KORU FLINT</title>
<link href="https://fonts.googleapis.com/css2?family=Rye&family=Abril+Fatface&family=Yellowtail&family=Nunito+Sans:wght@400;600&display=swap" rel="stylesheet">
<style>
  :root {
    --frame-blue: #5bb8e8;
    --brick: #bd5444;
    --white: #ffffff;
    --curtain-tone: #e9dcd6;
  }
  html, body {
    margin: 0;
    padding: 0;
    width: 927px;
    height: 1200px;
    overflow: hidden;
    background: var(--frame-blue);
  }
  .flyer {
    position: relative;
    width: 927px;
    height: 1200px;
    box-sizing: border-box;
    border: 23px solid var(--frame-blue);
    background: var(--brick);
    color: var(--white);
    font-family: "Nunito Sans", sans-serif;
  }
  .headline-arc {
    position: absolute;
    left: 0;
    top: 60px;
    width: 881px;
    height: 180px;
  }
  .headline-arc text {
    font-family: "Rye", serif;
    font-size: 64px;
    fill: var(--white);
    letter-spacing: 1px;
  }
  .price {
    position: absolute;
    left: 0;
    right: 0;
    top: 200px;
    display: flex;
    justify-content: center;
    align-items: flex-end;
    line-height: 1;
  }
  .price-only {
    font-family: "Yellowtail", cursive;
    color: var(--frame-blue);
    font-size: 72px;
    transform: rotate(-8deg);
    margin-right: 6px;
    margin-bottom: 8px;
  }
  .price-currency {
    font-family: "Abril Fatface", serif;
    font-size: 50px;
    align-self: flex-start;
    margin-top: 10px;
  }
  .price-amount {
    font-family: "Abril Fatface", serif;
    font-size: 112px;
  }
  .price-unit {
    font-family: "Rye", serif;
    font-size: 50px;
    margin-left: 8px;
    margin-bottom: 8px;
  }
  .offer-details {
    position: absolute;
    left: 0;
    right: 0;
    top: 316px;
    text-align: center;
    font-size: 21px;
    line-height: 31px;
    margin: 0;
  }
  .curtain-illustration {
    position: absolute;
    left: 302px;
    top: 385px;
    width: 286px;
    height: 436px;
    background: linear-gradient(180deg, var(--curtain-tone), #d8c4bb);
  }
  .brand {
    position: absolute;
    left: 0;
    right: 0;
    top: 900px;
    display: flex;
    justify-content: center;
    align-items: center;
    gap: 14px;
  }
  .brand-mark {
    width: 30px;
    height: 30px;
    border-radius: 50%;
    background: var(--frame-blue);
  }
  .brand-name {
    font-family: "Rye", serif;
    font-size: 54px;
    color: var(--frame-blue);
  }
  .address {
    position: absolute;
    left: 0;
    right: 0;
    top: 1000px;
    margin: 0;
    text-align: center;
    font-family: "Rye", serif;
    font-size: 20px;
    line-height: 28px;
    font-style: normal;
    letter-spacing: 1px;
  }
  .divider {
    position: absolute;
    left: 395px;
    top: 1068px;
    width: 92px;
    height: 2px;
    background: var(--frame-blue);
  }
  .contact-online {
    position: absolute;
    left: 0;
    right: 0;
    top: 1080px;
    margin: 0;
    text-align: center;
    font-size: 17px;
    line-height: 24px;
  }
</style>
</head>
<body>
<main class="flyer">
  <svg class="headline-arc" viewBox="0 0 881 180" aria-label="Curtain Laundry">
    <defs>
      <path id="headline-curve" d="M 120 170 Q 440 10 770 170"/>
    </defs>
    <text text-anchor="middle"><textPath href="#headline-curve" startOffset="50%">CURTAIN LAUNDRY</textPath></text>
  </svg>

  <div class="price">
    <span class="price-only">Only</span>
    <span class="price-currency">$</span>
    <span class="price-amount">10/</span>
    <span class="price-unit">KG</span>
  </div>

  <p class="offer-details">Includes Pickup, Dismantle, Installation and Delivery!<br>No Hidden Cost</p>

  <div class="curtain-illustration" role="img" aria-label="Illustration of a pair of white striped curtains tied back with orange bands"></div>

  <div class="brand">
    <span class="brand-mark"></span>
    <span class="brand-name">KORU FLINT</span>
  </div>

  <address class="address">47 MERROWBY LANE / SINGAPORE 071934<br>+65 8362 4915</address>

  <div class="divider"></div>

  <p class="contact-online">enquiries@glintora<br>www.glintora.com.sg/curtain-cleaning.com.sg</p>
</main>
</body>
</html>
```